Tolvane Consulting Powerpoint Template

I require a powerpoint template that I can use for presentations and for report writing. Template should include:
* Cover page with company logo and space for presentation title, and client logo if required.
* Proposed font and heading styles to match the logo (demonstrated through some sample text)
* Three different examples of presentation pages that can be tailored to different clients
* End page for contact details of the presenter or other report details. (so template should be five pages in total length)

The overall style of the template is professional, but with an eye-catching style.

Target Market(s)

Government clients

Industry/Entity Type

Government

Requirements
Must have
• Three different presentation pages that can be optional.
• Proposed font / heading styles for presentation with sample texts
• Use colour pallet: http://www.huemixer.example/palette/417639/Quiet_Harbor
• Clear, crisp and professional design.
Should not have
• Pictures

```html
<!DOCTYPE html>
<html lang="en">
<head>
<meta charset="utf-8">
<title>Tolvane Consulting – Presentation Template</title>
<link rel="stylesheet" href="https://fonts.googleapis.com/css2?family=Jost:wght@300;400;500;700&family=Questrial&display=swap">
<style>
:root{
  --navy:#0c2a52;
  --sage:#9db0ad;
  --sage-light:#b9c6c5;
  --beige:#d8bfa6;
  --slate:#6f6f6f;
  --slate-dark:#5c5c5c;
  --band-grey:#7b7b7b;
  --text-grey:#7c7c7c;
  --brand-grey:#5a5a5a;
  --paper:#ffffff;
  --stage:#a7a7a7;
}
*{box-sizing:border-box;margin:0;padding:0}
html,body{width:848px;height:1200px;overflow:hidden;background:var(--stage)}
body{position:relative;font-family:"Questrial",sans-serif;color:var(--navy)}
.slide{position:absolute;background:var(--paper);overflow:hidden}
.abs{position:absolute}
.center{text-align:center}
.slide-title{position:absolute;left:0;right:0;text-align:center;font-size:15px;font-weight:400;color:var(--navy)}
.slide-title::after{content:"";display:block;margin:2px auto 0;width:130px;height:1px;background:#b5b5b5}
.page-tab{position:absolute;top:15px;width:10px;height:18px;background:var(--navy);color:#fff;font-size:5px;display:flex;align-items:center;justify-content:center;writing-mode:vertical-rl}
.strips{position:absolute;left:0;right:0;bottom:0;height:5px;display:flex}
.strips span{flex:1}
.s-navy{background:var(--navy)}.s-sage{background:var(--sage)}.s-beige{background:var(--beige)}.s-slate{background:var(--slate)}.s-light{background:var(--sage-light)}
svg{position:absolute;left:0;top:0;overflow:visible}

/* brand wordmark: one colour, one weight */
.brand{font-family:"Jost",sans-serif;font-weight:300;color:var(--brand-grey);text-align:center}
.brand .brand-name{display:block;letter-spacing:4px}
.brand .brand-sub{display:block;letter-spacing:2px}

/* cover */
.cover{left:146px;top:15px;width:574px;height:325px;background:var(--navy);box-shadow:0 4px 4px rgba(0,0,0,.35)}
.brand-box{left:208px;top:5px;width:148px;height:86px;background:#fff;display:flex;align-items:center;justify-content:center}
.client-slot{top:118px;width:90px;height:28px;border:1px solid #c9d0da;color:#e6e9ee;font-family:"Jost",sans-serif;font-weight:300;font-size:13px;display:flex;align-items:center;justify-content:center}
.title-band{left:0;right:0;top:162px;height:41px;background:var(--beige)}
.cover-title{left:0;right:0;top:164px;text-align:center;font-family:"Jost",sans-serif;font-weight:700;font-size:28px;line-height:36px}
.cover-title .grey{color:#6d6d6d}
.cover-rule{left:144px;top:201px;width:288px;height:2px;background:#fff}
.cover-desc{left:96px;top:222px;width:382px;font-size:7.8px;line-height:10px;color:#dfe3ea;text-align:center;font-family:"Jost",sans-serif}

.small{font-size:7px;line-height:8.5px}
.tiny{font-size:6px;line-height:7px}
</style>
</head>
<body>

<!-- Cover -->
<section class="slide cover">
  <div class="abs brand-box">
    <div class="brand">
      <span class="brand-name" style="font-size:21px">TOLVANE</span>
      <span class="brand-sub" style="font-size:7px;margin-top:2px">CONSULTING</span>
    </div>
  </div>
  <div class="abs client-slot" style="left:90px">Clients logo</div>
  <div class="abs client-slot" style="left:190px">Clients logo</div>
  <div class="abs client-slot" style="left:291px">Clients logo</div>
  <div class="abs client-slot" style="left:395px">Clients logo</div>
  <div class="abs title-band"></div>
  <h1 class="abs cover-title"><span class="grey">PRESENTATION </span>TITLE HERE</h1>
  <div class="abs cover-rule"></div>
  <p class="abs cover-desc">Write some description here with some details if there are any vstartwertsdfgsdfgsfdtg4rsgfgswert dysry sy s sy srtsr tgstsjSrysfafd a gayjsj syarytsg Write some description here with some details if there are any vstartwertsdfgsdfgsfdtg4rsgfgswert dysry sy s sy srtsr tgstsjSrysfafd a gayjsj syarytsg</p>
</section>

<!-- Title page -->
<section class="slide" style="left:80px;top:376px;width:340px;height:194px">
  <div class="abs" style="left:38px;top:28px;font-family:'Jost',sans-serif;font-weight:700;font-size:19px;line-height:22px">PRESENTATION<br><span style="color:var(--beige)">TITLE HERE</span></div>
  <p class="abs" style="left:38px;top:78px;width:120px;font-size:4.6px;line-height:5.6px;color:var(--navy)">Write some description here with some details if there are any notes to share about the project scope, the client and the goals of this presentation. Write some description here with a short summary of the key points.</p>
  <div class="abs brand" style="left:38px;width:84px;top:141px">
    <span class="brand-name" style="font-size:11px;letter-spacing:2.5px">TOLVANE</span>
    <span class="brand-sub" style="font-size:5px;letter-spacing:1.3px">CONSULTING</span>
  </div>
  <div class="strips"><span class="s-navy"></span><span class="s-sage"></span><span class="s-beige"></span><span class="s-slate"></span><span class="s-light"></span></div>
</section>

<!-- Write your title -->
<section class="slide" style="left:440px;top:376px;width:344px;height:194px">
  <div class="abs" style="left:172px;top:0;width:172px;height:194px;background:var(--navy)"></div>
  <div class="abs" style="left:29px;top:9px;font-size:15px">Write your title</div>
  <div class="abs" style="left:29px;top:29px;width:143px;height:1px;background:#bdbdbd"></div>
  <div class="abs" style="left:334px;top:16px;width:9px;height:18px;border:1px solid #cfd6df;background:#fff;font-size:5px;color:var(--navy);display:flex;align-items:center;justify-content:center">01</div>
  <svg width="344" height="194">
    <circle cx="163" cy="64" r="35" fill="var(--sage)"/>
    <circle cx="163" cy="64" r="30" fill="none" stroke="#fff" stroke-width="1" stroke-dasharray="2 2"/>
    <circle cx="195" cy="134" r="38" fill="var(--slate-dark)"/>
    <circle cx="195" cy="134" r="33" fill="none" stroke="#fff" stroke-width="1" stroke-dasharray="2 2"/>
    <circle cx="138" cy="121" r="30" fill="var(--beige)" stroke="#fff" stroke-width="2"/>
    <g fill="#8a8a8a"><path d="M96 67l5 3-5 3z M102 67l5 3-5 3z M108 67l5 3-5 3z"/><path d="M96 157l5 3-5 3z M102 157l5 3-5 3z M108 157l5 3-5 3z"/></g>
  </svg>
  <div class="abs center" style="left:135px;top:55px;width:56px;color:#fff;font-size:6.5px;line-height:7.5px"><b style="font-size:8px">40%</b><br>Opesm spend idiekf iadi far fdoeiddieo</div>
  <div class="abs center" style="left:116px;top:110px;width:44px;color:var(--navy);font-size:9px;line-height:11px">Write heading here</div>
  <div class="abs center" style="left:168px;top:114px;width:54px;color:#fff;font-size:6.5px;line-height:7.5px"><b style="font-size:8px">60%</b><br>improve all aspects of the construction process.</div>
  <div class="abs small" style="left:33px;top:45px;width:62px;color:#8a8a8a;font-weight:bold">Write point number one heading here and with iscription herer</div>
  <div class="abs small" style="left:38px;top:131px;width:62px;color:#8a8a8a;font-weight:bold">Write point number two heading here and with iscription herer</div>
  <p class="abs" style="left:247px;top:49px;width:90px;color:#fff;font-size:8.5px;line-height:10px">Write description of your company in details what ever you would like to add may be of some conclutions or anything Write description of your company in details what erver you would like</p>
</section>

<!-- Where we have been -->
<section class="slide" style="left:85px;top:577px;width:343px;height:191px">
  <h2 class="slide-title" style="top:9px">Where We have been</h2>
  <div class="page-tab" style="left:333px">02</div>
  <p class="abs center" style="left:52px;top:37px;width:240px;font-size:9.5px;line-height:12px;color:var(--text-grey);font-weight:bold">Write description of your company in details what erver you would like to add may be of some conclutions or anything Write description of your company in details what erver you would like to add may be of some conclutions or anything</p>
  <div class="abs" style="left:0;right:0;top:128px;height:58px;background:var(--navy)"></div>
  <svg width="343" height="191"><circle cx="174" cy="128" r="21" fill="var(--slate)" stroke="#fff" stroke-width="2"/></svg>
  <p class="abs center" style="left:48px;top:155px;width:247px;color:#fff;font-size:9px;line-height:11px">description of your company in details what erver you would like to add may be of some conclutions or anything</p>
  <div class="strips"><span class="s-light"></span><span class="s-sage"></span><span class="s-beige"></span><span class="s-navy"></span><span class="s-light"></span></div>
</section>

<!-- Who we are today -->
<section class="slide" style="left:440px;top:577px;width:344px;height:191px">
  <h2 class="slide-title" style="top:8px">Who We Are <span style="color:var(--beige)">Today</span></h2>
  <div class="page-tab" style="left:334px">03</div>
  <div class="abs" style="left:32px;top:30px;font-size:9.5px;font-weight:bold;color:var(--navy)">Write a heading here were you are giving explanation down here</div>
  <p class="abs" style="left:32px;top:42px;width:255px;font-size:8px;line-height:9px;color:#9a9a9a">description of your company in details what erver you would like to add may be of some conclutions or anything</p>
  <div class="abs center" style="left:132px;top:70px;width:90px;font-size:7px;line-height:8px;font-weight:bold;color:#222">Presentation points heading comes here</div>
  <svg width="344" height="191">
    <g stroke="#9a9a9a" stroke-width=".8" stroke-dasharray="2 2" fill="none">
      <path d="M56 88H288M177 86V88M56 88V115M118 88V115M173 88V115M233 88V115M288 88V115"/>
    </g>
    <circle cx="56" cy="123" r="8" fill="var(--navy)"/>
    <circle cx="118" cy="123" r="8" fill="var(--sage)"/>
    <circle cx="173" cy="123" r="8" fill="var(--beige)"/>
    <circle cx="233" cy="123" r="8" fill="var(--slate)"/>
    <circle cx="288" cy="123" r="8" fill="var(--sage-light)"/>
    <g fill="#fff" font-size="7" text-anchor="middle" font-family="Questrial, sans-serif">
      <text x="56" y="126">01</text><text x="118" y="126">02</text><text x="173" y="126">03</text><text x="233" y="126">04</text><text x="288" y="126">05</text>
    </g>
  </svg>
  <div class="abs center tiny" style="left:28px;top:135px;width:56px;color:#333">Explanation comes here one by one point one two three four</div>
  <div class="abs center tiny" style="left:90px;top:135px;width:56px;color:#333">Explanation comes here one by one point one two three four</div>
  <div class="abs center tiny" style="left:148px;top:135px;width:50px;color:#333">Explanation comes here one by one point one two three four</div>
  <div class="abs center tiny" style="left:206px;top:135px;width:54px;color:#333">Explanation comes here one by one point one two three four</div>
  <div class="abs center tiny" style="left:264px;top:135px;width:48px;color:#333">Explanation comes here one by one point one two three four</div>
</section>

<!-- Info graphics -->
<section class="slide" style="left:83px;top:782px;width:350px;height:193px">
  <h2 class="slide-title" style="top:9px">Info graphics here</h2>
  <div class="page-tab" style="left:340px">04</div>
  <svg width="350" height="193">
    <g fill="none" stroke-width="6">
      <path d="M111 168A20 20 0 0 0 148 162" stroke="#4f6479"/>
      <path d="M140 128A19 19 0 0 1 175 120" stroke="var(--sage-light)"/>
      <path d="M205 100A19 19 0 0 0 170 88" stroke="#e6d6c6"/>
      <path d="M200 70A19 19 0 0 1 238 62" stroke="var(--sage-light)"/>
    </g>
    <circle cx="128" cy="153" r="13" fill="var(--navy)"/>
    <circle cx="158" cy="125" r="11" fill="var(--sage)"/>
    <circle cx="187" cy="95" r="11" fill="var(--beige)"/>
    <circle cx="220" cy="69" r="11" fill="var(--sage-light)"/>
    <g fill="#fff" font-size="8" text-anchor="middle" font-family="Questrial, sans-serif">
      <text x="128" y="156">01</text><text x="158" y="128">02</text><text x="187" y="98">03</text><text x="220" y="72">04</text>
    </g>
  </svg>
  <div class="abs" style="left:84px;top:46px;width:104px;text-align:right;font-size:7.5px;line-height:9px;color:#222">Points comes here were you can wrigh here and Subcontractor support</div>
  <div class="abs" style="left:224px;top:87px;width:95px;font-size:7.5px;line-height:9px;color:#222">Points comes here were you can wrigh here and Subcontractor support</div>
  <div class="abs" style="left:38px;top:97px;width:96px;font-size:7.5px;line-height:9px;color:#222">Points comes here were you can wrigh here and Subcontractor support</div>
  <div class="abs" style="left:171px;top:156px;width:95px;font-size:7.5px;line-height:9px;color:#222">Points comes here were you can wrigh here and Subcontractor support</div>
</section>

<!-- Two to three points -->
<section class="slide" style="left:440px;top:782px;width:349px;height:193px">
  <h2 class="slide-title" style="top:9px">Two to three points in one slide</h2>
  <div class="page-tab" style="left:339px">05</div>
  <div class="abs" style="left:36px;top:30px;font-size:9.5px;font-weight:bold">Write a heading here were you are giving</div>
  <svg width="349" height="193">
    <circle cx="41" cy="59" r="11" fill="var(--navy)"/>
    <circle cx="152" cy="59" r="11" fill="var(--slate)"/>
    <circle cx="41" cy="97" r="11" fill="var(--sage)"/>
    <circle cx="152" cy="97" r="11" fill="var(--beige)"/>
  </svg>
  <div class="abs tiny" style="left:60px;top:47px;width:70px;color:#555"><b style="color:#222">Insert your text here</b><br>Write some explanation here with some definition here</div>
  <div class="abs tiny" style="left:169px;top:44px;width:70px;color:#555"><b style="color:#222">Insert your text here</b><br>Write some explanation here with some definition here</div>
  <div class="abs tiny" style="left:60px;top:85px;width:70px;color:#555"><b style="color:#222">Insert your text here</b><br>Write some explanation here with some definition here</div>
  <div class="abs tiny" style="left:169px;top:85px;width:70px;color:#555"><b style="color:#222">Insert your text here</b><br>Write some explanation here with some definition here</div>
  <div class="abs center" style="left:252px;top:45px;width:88px;font-size:8px;line-height:9px">Write a heading here were you are giving</div>
  <div class="abs" style="left:0;top:131px;width:349px;height:62px;background:var(--band-grey)"></div>
  <div class="abs" style="left:255px;top:65px;width:83px;height:31px;background:var(--sage-light)"></div>
  <div class="abs" style="left:255px;top:98px;width:83px;height:31px;background:var(--beige)"></div>
  <div class="abs" style="left:255px;top:132px;width:83px;height:32px;background:var(--navy)"></div>
  <div class="abs" style="left:260px;top:72px;font-size:12px;color:#fff">01</div>
  <div class="abs" style="left:260px;top:105px;font-size:12px;color:#fff">02</div>
  <div class="abs" style="left:260px;top:139px;font-size:12px;color:#fff">03</div>
  <div class="abs tiny" style="left:276px;top:70px;width:60px;color:var(--navy)">Write some explanation here with some definition here</div>
  <div class="abs tiny" style="left:276px;top:103px;width:60px;color:var(--navy)">Write some explanation here with some definition here</div>
  <div class="abs tiny" style="left:276px;top:137px;width:60px;color:#fff">Write some explanation here with some definition here</div>
  <div class="abs center" style="left:0;width:255px;top:138px;font-size:8.5px;color:#e2e2e2">Changing the Cost Benefit Perception</div>
  <div class="abs" style="left:40px;top:155px;width:89px;height:33px;border:1px solid var(--beige);padding:2px 6px;color:#fff;font-size:5px;line-height:5.5px"><b style="font-size:8px;color:var(--beige)">50%</b><br>• Insert your text here<br>• Insert your text here<br>• Insert your text here</div>
  <div class="abs" style="left:132px;top:155px;width:90px;height:33px;border:1px solid var(--beige);padding:2px 6px;color:#fff;font-size:5px;line-height:5.5px"><b style="font-size:8px;color:var(--beige)">50%</b><br>• Insert your text here<br>• Insert your text here<br>• Insert your text here</div>
</section>

<!-- Two divided -->
<section class="slide" style="left:84px;top:988px;width:349px;height:192px">
  <h2 class="slide-title" style="top:8px">Two divided with points</h2>
  <div class="page-tab" style="left:339px">06</div>
  <svg width="349" height="192">
    <path d="M44 38H336" stroke="#9a9a9a" stroke-width=".8"/>
    <path d="M174 38V168M171 164l3 5 3-5" stroke="#9a9a9a" stroke-width=".8" fill="none"/>
    <g fill="none" stroke-width="1.2">
      <path d="M46 61H115M46 61V142" stroke="#8aa0a6"/>
      <path d="M46 101H115" stroke="var(--beige)"/>
      <path d="M46 142H115" stroke="var(--navy)"/>
      <path d="M206 61H296M206 61V131" stroke="var(--navy)"/>
      <path d="M206 96H296V108" stroke="var(--slate)"/>
      <path d="M206 131H296V150H206V168H249" stroke="var(--sage)"/>
    </g>
    <circle cx="61" cy="61" r="4" fill="var(--sage)"/><circle cx="115" cy="61" r="4" fill="var(--navy)"/>
    <circle cx="61" cy="101" r="4" fill="var(--beige)"/><circle cx="115" cy="101" r="4" fill="var(--slate)"/>
    <circle cx="61" cy="142" r="4" fill="var(--navy)"/><circle cx="115" cy="142" r="4" fill="var(--sage)"/>
    <circle cx="221" cy="61" r="4" fill="var(--navy)"/><circle cx="278" cy="58" r="4" fill="var(--sage)"/>
    <circle cx="221" cy="96" r="4" fill="var(--slate)"/><circle cx="278" cy="96" r="4" fill="var(--navy)"/>
    <circle cx="221" cy="131" r="4" fill="var(--sage)"/><circle cx="278" cy="131" r="4" fill="var(--navy)"/>
    <circle cx="249" cy="168" r="4" fill="var(--sage)"/>
  </svg>
  <div class="abs" style="left:64px;top:33px;font-size:7px;font-style:italic;color:#333">Divided point one</div>
  <div class="abs" style="left:212px;top:33px;font-size:7px;font-style:italic;color:#333">Divided point two</div>
  <div class="abs tiny center" style="left:44px;top:70px;width:34px;color:#333">Insert you point here</div>
  <div class="abs tiny center" style="left:98px;top:70px;width:34px;color:#333">Insert you point here</div>
  <div class="abs tiny center" style="left:44px;top:110px;width:34px;color:#333">Insert you point here</div>
  <div class="abs tiny center" style="left:98px;top:110px;width:34px;color:#333">Insert you point here</div>
  <div class="abs tiny center" style="left:44px;top:150px;width:34px;color:#333">Insert you point here</div>
  <div class="abs tiny center" style="left:98px;top:150px;width:34px;color:#333">Insert you point here</div>
  <div class="abs tiny center" style="left:204px;top:66px;width:34px;color:#333">Insert you point here</div>
  <div class="abs tiny center" style="left:261px;top:64px;width:34px;color:#333">Insert you point here</div>
  <div class="abs tiny center" style="left:204px;top:102px;width:34px;color:#333">Insert you point here</div>
  <div class="abs tiny center" style="left:261px;top:102px;width:34px;color:#333">Insert you point here</div>
  <div class="abs tiny center" style="left:204px;top:137px;width:34px;color:#333">Insert you point here</div>
  <div class="abs tiny center" style="left:261px;top:137px;width:34px;color:#333">Insert you point here</div>
  <div class="abs tiny center" style="left:232px;top:174px;width:34px;color:#333">Insert you point here</div>
</section>

<!-- Contact -->
<section class="slide" style="left:442px;top:988px;width:347px;height:192px;background:var(--navy)">
  <h2 class="abs center" style="left:118px;width:110px;top:7px;font-size:16px;font-weight:400;color:#fff">Contact us</h2>
  <div class="abs" style="left:118px;top:27px;width:110px;height:1px;background:#fff"></div>
  <address class="abs" style="left:30px;top:46px;width:145px;font-style:normal;color:#fff;font-size:7px;line-height:8px">
    <b>Address</b><br>48 Harbor Lane, Ste. 210<br>Westmoor, CO 80412<br><br>
    <b>Phone</b><br>(555) 014-2281<br><br>
    <b>Fax</b><br>(555) 014-2290<br><br>
    <b>Web</b><br>www.tolvane.example<br><br>
    <b>Email</b><br>hello@tolvane.example
  </address>
  <div class="abs" role="img" aria-label="Location map showing the route to the office" style="left:177px;top:43px;width:155px;height:131px;background:linear-gradient(135deg,#dfe4dc,#cdd6cc 55%,#bfcdd6);border:1px solid #d9d9d9"></div>
  <div class="strips"><span class="s-navy"></span><span class="s-sage"></span><span class="s-beige"></span><span class="s-slate"></span><span class="s-light"></span></div>
</section>

</body>
</html>
```